Personal Business Card

I am an award winning banjo player who plays with two different professional bands. My experiences include studio recordings for other artists and played the theme song for the Creature Channel's "Frontier Tundra Trails". I am ready to take my career to the next level and would like something that will look professional. it is important to me to have a banjo on the card. If possible my accomplishments to be put on back of card.

Industry/Entity Type

Artists

Contact Information for Business Card

Corbin Halloway
cell 602-315-2860
email corbinhallowaybanjo@mailvista.net

2008 AZ Banjo Champion
2008 Pinebrook Banjo Champion
2010 AZ Banjo Champion
2010 Riverbend Hoedown Talcott Banjo Champion
2010 Cedar Hollow Gathering Banjo Finalist

```html
<!DOCTYPE html>
<html lang="en">
<head>
<meta charset="utf-8">
<title>Corbin Halloway – Banjo</title>
<link rel="stylesheet" href="https://fonts.googleapis.com/css2?family=Open+Sans:wght@400;600&display=swap">
<style>
  :root {
    --card-white: #ffffff;
    --band-black: #1b1d1f;
    --accent-orange: #f9a811;
    --tab-grey: #e9e8e6;
    --ink-dark: #1c1f21;
    --art-light: #ececea;
    --art-mid: #d9d9d6;
  }
  html, body {
    margin: 0;
    padding: 0;
    overflow: hidden;
    background: var(--card-white);
  }
  .card {
    position: relative;
    width: 1200px;
    height: 702px;
    overflow: hidden;
    background: var(--card-white);
    font-family: "Open Sans", Arial, sans-serif;
  }
  .banjo-art {
    position: absolute;
    left: 180px;
    top: 10px;
    width: 860px;
    height: 520px;
    border-radius: 260px 220px 40px 260px;
    background: radial-gradient(ellipse at 30% 68%, var(--art-mid) 0%, var(--art-light) 45%, rgba(255,255,255,0) 75%);
  }
  .card-shapes {
    position: absolute;
    inset: 0;
    width: 1200px;
    height: 702px;
  }
  .accent-line, .accent-block { fill: var(--accent-orange); }
  .contact-band { fill: var(--band-black); }
  .name-tab { fill: var(--tab-grey); }
  .name-mark {
    position: absolute;
    left: 758px;
    top: 142px;
    height: 124px;
    display: flex;
    align-items: center;
    gap: 14px;
  }
  .name-mark__dot {
    width: 36px;
    height: 36px;
    border-radius: 50%;
    background: var(--ink-dark);
  }
  .name-mark__text {
    margin: 0;
    font-size: 44px;
    font-weight: 400;
    color: var(--ink-dark);
    letter-spacing: -0.3px;
    white-space: nowrap;
  }
  .contact-list {
    position: absolute;
    left: 82px;
    top: 560px;
    display: flex;
    gap: 56px;
    margin: 0;
    padding: 0;
    list-style: none;
    color: var(--card-white);
    font-size: 25px;
  }
  .contact-list__item {
    display: flex;
    align-items: center;
    gap: 12px;
  }
  .contact-icon { width: 30px; height: 24px; fill: var(--card-white); }
</style>
</head>
<body>
<div class="card">
  <div class="banjo-art" role="img" aria-label="Illustration of a banjo angled up to the right"></div>

  <svg class="card-shapes" viewBox="0 0 1200 702" aria-hidden="true">
    <path class="accent-line" d="M0 509 H762 Q784 509 792 524 L0 524 Z"/>
    <path class="contact-band" d="M0 517 H772 Q792 517 800 534 L882 702 H0 Z"/>
    <path class="accent-block" d="M850 549 H1200 V702 H925 Z"/>
    <path class="name-tab" d="M752 142 H1200 V266 H692 L738 153 Q743 142 752 142 Z"/>
  </svg>

  <div class="name-mark">
    <span class="name-mark__dot"></span>
    <h1 class="name-mark__text">Corbin Halloway</h1>
  </div>

  <ul class="contact-list">
    <li class="contact-list__item">
      <svg class="contact-icon" viewBox="0 0 30 24" aria-hidden="true">
        <path d="M2 8 Q15 -1 28 8 L26 11 L20 9 L20 7 Q15 5 10 7 L10 9 L4 11 Z"/>
        <path d="M8 12 H22 L26 22 H4 Z"/>
      </svg>
      <span>602-315-2860</span>
    </li>
    <li class="contact-list__item">
      <svg class="contact-icon" viewBox="0 0 30 24" aria-hidden="true">
        <path d="M1 2 H29 V22 H1 Z M4 5 L15 14 L26 5 M4 19 L11 12 M26 19 L19 12" fill="none" stroke="#ffffff" stroke-width="2.2"/>
      </svg>
      <span>corbinhallowaybanjo@mailvista.net</span>
    </li>
  </ul>
</div>
</body>
</html>
```